Larkspur Homes - wanted BRILLIANT website design for our new property investing company

We need a website design for our new company based in Bristol, England, UK called "Larkspur Homes". We help buy people property who are in financial difficulty or who are needing to sell their property quickly for reasons such as death, divorce/separation, relocation, emigration.

We have a logo being designed incorporating strawberry and property (so red and green). We would like designs to communicate an elegant ,professional, approachable, friendly
fresh clean but also warm appealing appearance
Not too busy
Website consistent with logo and company name i.e. colour scheme

Please use our word document for content as a guide but use professional judgement for minor alterations if you feel they would benefit the site/structure etc

Please ask at any time if not sure

Target Market(s)

Adult british population, those that have a mortgage / loan / own property

Industry/Entity Type

Financial

Font styles to use
Serif
Sans Serif
Decorative

Colors
0692cd
33b7a4
acd036
fbee3e
3176b5
886aae
a6479a
e567a6
eb1f27

Requirements
Must have
• This must not look like a template website we are looking for UNIQUE please!
Nice to have
• Bristol pictures instead of generic, or colourful line drawings/comic drawings of houses/property/keys/happy people.....
Should not have
• An obvious off the shelf template design

```html
<!DOCTYPE html>
<html lang="en">
<head>
<meta charset="utf-8">
<title>Larkspur Homes</title>
<link href="https://fonts.googleapis.com/css2?family=Arvo:wght@400;700&family=Open+Sans:wght@400;600&family=PT+Sans+Narrow:wght@400;700&display=swap" rel="stylesheet">
<style>
:root{
  --red:#c4202b;
  --red-text:#c4524a;
  --green:#8cbd1b;
  --green-dark:#6ea313;
  --blue:#0a72b9;
  --yellow:#f8b31a;
  --purple:#9b3fa0;
  --pink:#d2357a;
  --cream:#fdfce8;
  --ink:#444;
  --grey-band:#ebebeb;
  --grey-bar:#5e5e5e;
}
*{box-sizing:border-box;margin:0;padding:0}
html,body{width:735px;height:1200px;overflow:hidden;background:#fff}
body{position:relative;font-family:'Open Sans',sans-serif;color:var(--ink)}
.abs{position:absolute}

/* header */
.header{left:0;top:0;width:735px;height:266px}
.header-art{position:absolute;inset:0;background:linear-gradient(180deg,#dff2f8 0%,#eef8fb 30%,#f2e3cf 55%,#e9c4a3 75%,#f5efe6 100%)}
.brand{left:14px;top:44px;font-family:'Arvo',serif;font-size:15px;color:var(--red);display:flex;align-items:center;gap:6px}
.brand-dot{width:12px;height:12px;border-radius:50%;background:var(--red)}
.callout{right:30px;top:24px;text-align:right}
.callout small{font-size:9px;color:#333;display:block}
.callout .phone{font-size:21px;font-weight:600;color:#222;display:flex;align-items:center;gap:4px;justify-content:flex-end;line-height:1.1}
.callout .mail{font-size:9px;color:var(--green-dark)}

/* nav */
.nav{left:0;top:266px;width:735px;height:29px;background:var(--red);font-family:'Arvo',serif;font-size:10.5px;color:#fff}
.nav a{position:absolute;top:0;color:#fff;text-decoration:none;height:29px;line-height:29px;white-space:nowrap}
.nav a.current{background:var(--green);left:4px;width:63px;text-align:center}

/* hero */
.hero{left:0;top:295px;width:735px;height:301px;background:var(--cream)}
.hero h1{position:absolute;left:19px;top:31px;width:420px;font-family:'Arvo',serif;font-size:27px;line-height:27px;color:var(--red-text);word-spacing:5px;font-weight:700}
.hero .lead{position:absolute;left:18px;top:110px;font-size:13.5px;color:#555;word-spacing:2px}
.bullets{position:absolute;top:143px;list-style:none;font-size:10.4px;color:#555;line-height:11px}
.bullets li{padding-left:14px;position:relative;margin-bottom:7px}
.bullets li::before{content:"";position:absolute;left:1px;top:2px;border-left:5px solid #c4524a;border-top:3.5px solid transparent;border-bottom:3.5px solid transparent}
.col-a{left:28px;width:170px}
.col-b{left:233px;width:200px}

.form{left:481px;top:34px;width:231px;height:249px;background:var(--green);border-radius:4px}
.form-tab{position:absolute;left:38px;top:-13px;width:165px;height:40px}
.field{position:absolute;left:16px;width:199px;height:22px;background:#fff;border:1px solid #e7e7d2;font-family:'Arvo',serif;font-size:9.5px;color:var(--green-dark);padding:4px 7px}
.submit{position:absolute;left:16px;top:222px;width:199px;height:20px;background:var(--blue);color:#fff;font-family:'Arvo',serif;font-size:10px;text-align:center;line-height:20px}

/* steps */
.steps{left:16px;top:616px;width:700px;height:210px}
.step{position:absolute;top:27px;width:136px;height:180px;color:#fff;padding:26px 8px 0 21px;font-family:'PT Sans Narrow',sans-serif}
.step h3{font-size:13px;font-weight:700;line-height:16px;margin-bottom:6px;letter-spacing:.2px}
.step p{font-size:9px;line-height:12.2px;margin-bottom:11px}
.badge{position:absolute;top:-27px;width:48px;height:48px;border-radius:50%;background:#fff;border:5px solid;display:flex;align-items:center;justify-content:center;font-family:'PT Sans Narrow',sans-serif;font-weight:700;font-size:26px}
.s1{left:26px;background:var(--yellow)}.s1 .badge{border-color:var(--yellow);color:var(--yellow);left:-26px}
.s2{left:160px;background:var(--purple)}.s2 .badge{border-color:var(--purple);color:var(--purple);left:-26px}
.s3{left:294px;background:var(--blue)}.s3 .badge{border-color:var(--blue);color:var(--blue);left:-26px}
.s4{left:428px;background:var(--pink)}.s4 .badge{border-color:var(--pink);color:var(--pink);left:-26px}
.s5{left:562px;background:var(--green);width:132px}.s5 .badge{border-color:var(--green);color:var(--green);left:-26px}
.s3{top:20px;height:187px;padding-top:22px}

/* help */
.help h2{position:absolute;left:26px;top:850px;font-family:'Arvo',serif;font-size:27px;color:#333}
.help-list{position:absolute;top:904px;list-style:none;font-size:10.4px;color:#444}
.help-list li{height:25.3px;padding-left:12px;position:relative}
.help-list li::before{content:"›";position:absolute;left:0;top:-2px;color:var(--red);font-weight:700;font-size:12px}

/* footer */
.footer{left:0;top:1033px;width:735px;height:135px;background:var(--grey-band)}
.foot-brand{position:absolute;left:22px;top:64px;font-family:'Arvo',serif;font-size:11px;color:#555;display:flex;align-items:center;gap:5px}
.foot-brand i{width:10px;height:10px;border-radius:50%;background:#666;display:block}
.foot-h{position:absolute;top:24px;font-size:13px;font-weight:600;color:#333;letter-spacing:.3px}
.foot-links{position:absolute;top:57px;font-family:Arial,sans-serif;font-size:8.5px;line-height:10.8px;color:#555}
.badge-shape{position:absolute;background:#7a7a7a}
.bar{left:0;top:1168px;width:735px;height:32px;background:var(--grey-bar);color:#ddd;font-family:Arial,sans-serif;font-size:8.5px;padding:12px 19px}
.social{position:absolute;top:8px;width:17px;height:17px;border-radius:50%;background:#9a9a9a}
</style>
</head>
<body>

<header class="header abs">
  <div class="header-art" role="img" aria-label="Colourful illustrated row of terraced houses with pitched roofs under a pale sky"></div>
  <div class="brand abs"><span class="brand-dot"></span>Larkspur Homes</div>
  <div class="callout abs">
    <small>For questions call us</small>
    <div class="phone">
      <svg width="17" height="17" viewBox="0 0 20 20"><circle cx="10" cy="10" r="8.5" fill="none" stroke="#222" stroke-width="1.8"/><path d="M7 5.5c-.8.4-1.3 1.3-1 2.4.8 2.8 3 5 5.7 5.9 1.1.3 2-.2 2.5-1l-1.6-1.5-1.3.8c-1.3-.6-2.3-1.6-2.9-2.9l.8-1.3z" fill="#222"/></svg>
      0117-4630
    </div>
    <div class="mail">hello@larkspur-homes.co.uk</div>
  </div>
</header>

<nav class="nav abs">
  <a class="current">Home</a>
  <a style="left:81px">Sell Your Property Fast</a>
  <a style="left:221px">Rent Your Property Fast</a>
  <a style="left:366px">The 5 Easy Stpes</a>
  <a style="left:476px">Common Questions</a>
  <a style="left:602px">About Us</a>
  <a style="left:673px">Contact</a>
</nav>

<section class="hero abs">
  <h1>Do you want to sell or rent out your house quickly?</h1>
  <p class="lead">We are a local family run property business who specialize in</p>
  <ul class="bullets col-a">
    <li>Buying properties quickly</li>
    <li>Finding creative solutions to your property problems</li>
    <li>Property rental management</li>
    <li>STOPPING repossession</li>
    <li>Motivated sellers</li>
  </ul>
  <ul class="bullets col-b">
    <li>Lettings to professional and student tenants</li>
    <li>Guaranteed rent and agement schemes for landlord</li>
    <li>Chain fixing</li>
    <li>Negative equity problem</li>
  </ul>

  <form class="form abs">
    <svg class="form-tab" viewBox="0 0 165 40"><path d="M8 0h149l-8 10v30H16V10z" fill="#0a5fa0"/><path d="M0 0h165l-12 30H12z" fill="var(--blue)"/></svg>
    <span class="abs" style="left:38px;width:165px;top:-6px;text-align:center;color:#fff;font-size:13px">REQUEST</span>
    <span class="abs" style="left:38px;width:165px;top:10px;text-align:center;color:#fff;font-size:10px">Free Evaluation</span>
    <div class="field" style="top:40px">Name *</div>
    <div class="field" style="top:65px">Email *</div>
    <div class="field" style="top:90px">Phone Number *</div>
    <div class="field" style="top:115px">Property Address *</div>
    <div class="field" style="top:140px;height:71px">Message</div>
    <div class="submit">Submit</div>
  </form>
</section>

<section class="steps abs">
  <div class="step s1"><div class="badge">1</div><h3>CONTACT US</h3><p>Call our friendly team anytime OR fill in your contact details (above).</p><p>We will take your details and one of our expert team will be in contact within 48hrs. Usually within a very short</p></div>
  <div class="step s2"><div class="badge">2</div><h3>FREE CONSULTATION</h3><p>This is at a suitable time for yourself in your own home. We can view the property and have preliminary discussions into your problem and possible solutions.</p></div>
  <div class="step s3"><div class="badge">3</div><h3>GURANTEED OFFER</h3><p>We will organize a formal NCVB (National Council of Valuation Bodies) valuation. This is to protect you and us and ensure we have an accurate valuation of your home.</p><p>At this point we can give you a guaranteed</p></div>
  <div class="step s4"><div class="badge">4</div><h3>LEGAL STUFF</h3><p>There will be paperwork to fill</p><p>Solicitors from both sides (yours and ours) will ensure the deal is made into a formal contract</p></div>
  <div class="step s5"><div class="badge">5</div><h3>COMPLETION AND MONEY IN BANK</h3><p>Contracts are exchanged Completion date arranged Your problems are solve</p></div>
</section>

<section class="help">
  <h2>Who Can we Help?</h2>
  <ul class="help-list" style="left:35px"><li>How to stop repossession</li><li>Divorce or separation</li><li>Financial problems</li><li>Chain Collapse</li></ul>
  <ul class="help-list" style="left:205px"><li>Don't like estate agents?</li><li>Property needing work</li><li>Retiring landlords</li><li>Tenanted Property</li></ul>
  <ul class="help-list" style="left:375px"><li>Negative equity</li><li>Opportunity not to be missed!!</li><li>Guaranteed rent scheme</li></ul>
  <ul class="help-list" style="left:591px"><li>Ill health</li><li>Relocating</li><li>Inherited property</li></ul>
</section>

<footer class="footer abs">
  <div class="foot-brand"><i></i>Larkspur Homes</div>
  <div class="foot-h" style="left:172px">SITE NAV</div>
  <div class="foot-links" style="left:172px">Home<br>Sell Your Property Fast<br>Rent Your Property Fast<br>The 5 Easy Stpes</div>
  <div class="foot-links" style="left:287px">Common Questions<br>About Us<br>Contact</div>
  <div class="foot-h" style="left:410px">AFFILIATED ORGS</div>
  <div class="badge-shape" style="left:405px;top:58px;width:38px;height:46px;border-radius:50%"></div>
  <div class="badge-shape" style="left:456px;top:58px;width:36px;height:46px"></div>
  <div class="badge-shape" style="left:500px;top:67px;width:65px;height:22px"></div>
  <div class="foot-h" style="left:586px">Call us free on</div>
  <div class="abs" style="left:586px;top:57px;font-size:13px;color:#444">0800 318264</div>
  <div class="abs" style="left:586px;top:76px;font-family:Arial,sans-serif;font-size:8.5px;color:#555">hello@larkspur-homes.co.uk</div>
</footer>

<div class="bar abs">© 2014 Larkspur Homes Limited. Reg No 7731460
  <span class="social" style="left:602px"></span>
  <span class="social" style="left:625px"></span>
  <span class="social" style="left:648px"></span>
  <span class="social" style="left:672px"></span>
  <span class="social" style="left:696px"></span>
</div>

</body>
</html>
```